Wirenexa

I'm looking to much improve our current website wirenexa.com
Updates

Low design quality

Target Market(s)

Commercial clients (Not-Residentials)

Industry/Entity Type

Office buildings and Industrial clients

Coding

Coded - Design and coding required

Number of Pages Required

5+ page

Requirements
Must have
• Very professional structured low voltage cabling projects for Wi-Fi, Audio/Video conference rooms, Access Control systems, CCTV.

```html
<!DOCTYPE html>
<html lang="en">
<head>
<meta charset="utf-8">
<title>Wirenexa – Professional Low Voltage Cabling</title>
<link href="https://fonts.googleapis.com/css2?family=Lexend:wght@300;400;500;600;700&display=swap" rel="stylesheet">
<style>
:root{
  --red:#d8302b;
  --red-dark:#b8231f;
  --black:#0c0c0c;
  --ink:#161616;
  --muted:#555;
  --light:#f6f5f6;
  --white:#fff;
  --line:#d9d9d9;
}
*{margin:0;padding:0;box-sizing:border-box}
html,body{width:1200px;height:4412px;overflow:hidden}
body{font-family:"Lexend",sans-serif;color:var(--ink);background:var(--white);position:relative}
.abs{position:absolute}
a{color:inherit;text-decoration:none}

/* buttons */
.btn{position:absolute;display:flex;align-items:center;justify-content:center;gap:8px;border-radius:30px;font-size:11px;font-weight:500;height:30px}
.btn-red{background:var(--red);color:var(--white)}
.btn-outline{background:var(--white);color:var(--ink);border:1.5px solid #bbb}
.btn-black{background:var(--black);color:var(--white);font-size:10px;height:28px}
.btn svg{width:12px;height:12px}

/* header */
.topbar{left:856px;top:0;width:344px;height:24px;background:#2a2a2a;border-bottom-left-radius:14px;display:flex;align-items:center;padding-left:36px;gap:8px;color:#fff;font-size:10px}
.topbar .dot{width:15px;height:15px;border-radius:50%;background:#fff}
.topbar .phone{margin-right:16px;display:flex;gap:6px;align-items:center}
.brand{display:flex;align-items:center;gap:8px;font-weight:600;color:var(--ink);font-size:27px;letter-spacing:-.5px}
.brand .mark{width:26px;height:26px;border-radius:50%;border:4px solid var(--red)}
.nav{left:626px;top:42px;display:flex;gap:26px;font-size:10.5px;font-weight:500}
.nav .active{color:var(--red)}

/* hero */
.hero{left:0;top:75px;width:1200px;height:640px;background:linear-gradient(100deg,#1c2430 0%,#3a3f44 40%,#6b6a5e 70%,#8a8470 100%)}
.hero-title{left:106px;top:210px;width:640px;color:#fff;font-size:41px;font-weight:700;line-height:50px;letter-spacing:.2px}
.quote-frame{left:793px;top:197px;width:299px;height:418px;border:2px solid var(--red)}
.quote-card{left:769px;top:171px;width:299px;height:419px;background:var(--red);border-radius:6px;color:#fff;text-align:center;padding:30px 24px 0}
.quote-card h3{font-size:21px;font-weight:600}
.quote-card p{font-size:9.5px;margin-top:4px;opacity:.9}
.field{background:#fff;border-radius:18px;height:30px;margin-top:14px;color:#333;font-size:9.5px;text-align:left;padding:9px 14px}
.field:first-of-type{margin-top:18px}
.field.area{height:86px;border-radius:20px}
.quote-card .submit{position:static;margin:16px auto 0;width:104px;height:30px;background:var(--black);color:#fff;border-radius:20px;font-size:9.5px;display:flex;align-items:center;justify-content:center}
.callus{margin-top:20px;font-size:11px;display:flex;align-items:center;justify-content:center;gap:8px}
.callus .ic{width:20px;height:20px;border-radius:50%;background:#fff;display:flex;align-items:center;justify-content:center}

/* sections */
.section-light{left:0;width:1200px;background:var(--light)}
.eyebrow{position:absolute;left:0;width:1200px;text-align:center;color:var(--red);font-size:11px;font-weight:500;letter-spacing:.5px}
.heading{position:absolute;left:0;width:1200px;text-align:center;font-size:29px;font-weight:500;line-height:35px}

/* why cards */
.why-card{top:779px;width:250px;height:132px;background:#fff;border:1.5px solid #9a9a9a;text-align:center;padding-top:16px}
.why-card::before{content:"";position:absolute;left:0;top:0;border-top:16px solid var(--red);border-right:16px solid transparent}
.why-card::after{content:"";position:absolute;left:110px;bottom:-1px;width:30px;height:3px;background:var(--black)}
.why-card svg{width:38px;height:38px}
.why-card h4{font-size:13px;font-weight:500;margin-top:6px}
.why-card p{font-size:9px;color:var(--muted);line-height:15px;margin:6px auto 0;width:190px}

/* about */
.about-photo{left:203px;top:1116px;width:360px;height:360px;border-radius:50%;background:radial-gradient(circle at 50% 45%,#6f8fd0 0%,#3c5fa8 50%,#1f3566 100%);box-shadow:0 0 0 6px #fff,0 0 0 8px #e6e6e6}
.about{left:613px;top:1164px;width:380px}
.about .eyebrow{position:static;width:auto;text-align:left}
.about h2{font-size:29px;font-weight:600;margin-top:10px}
.about h5{font-size:13px;font-weight:500;line-height:19px;margin-top:16px}
.about p{font-size:9px;color:var(--muted);line-height:19px;margin-top:14px}
.about .btn{position:relative;width:104px;margin-top:22px}

/* services */
.svc-text h3{font-size:24px;font-weight:500}
.svc-text p{font-size:13.5px;color:#333;line-height:23px;margin-top:14px}
.svc-text .btn{position:relative;width:96px;margin-top:20px}
.photo{position:absolute}

/* projects */
.proj{top:2975px;width:182px;height:205px;background:#fff;border:1px solid #e3e3e3;text-align:center}
.proj .ph{height:155px}
.proj span{display:block;font-size:10px;font-weight:500;margin-top:12px;line-height:13px}

/* locations */
.loc{top:3485px;width:250px;height:175px}
.loc .tag{position:absolute;left:0;bottom:16px;background:#fff;padding:9px 30px 9px 12px;border-radius:0 20px 20px 0;font-size:10px;font-weight:600}

/* footer */
.footer{left:0;top:3880px;width:1200px;height:532px;background:var(--black);color:#fff}
.foot-nav{left:200px;top:4059px;width:800px;height:52px;border-top:1px solid #444;border-bottom:1px solid #444;display:flex;justify-content:center;align-items:center;gap:20px;font-size:9.5px;color:#ddd}
.foot-nav .active{color:var(--red)}
.foot-nav i{font-style:normal;color:#888}
.contact{top:4140px;width:262px;text-align:center}
.contact .ring{width:66px;height:66px;border-radius:50%;border:2px solid var(--red);margin:0 auto;display:flex;align-items:center;justify-content:center}
.contact .ring svg{width:26px;height:26px}
.contact h6{color:var(--red);font-size:11.5px;font-weight:500;margin-top:14px}
.contact p{font-size:10.5px;margin-top:4px;line-height:14px}
.divider{top:4144px;width:1px;height:126px;background:#555}
.socials{left:0;top:4300px;width:1200px;display:flex;justify-content:center;gap:10px}
.socials span{width:30px;height:30px;border-radius:50%;border:1.5px solid #fff}
.socials-line{top:4315px;height:1px;background:#444}
.copy{left:0;top:4361px;width:1200px;text-align:center;font-size:9px;color:#ccc}
.copy b{color:var(--red);font-weight:500}
</style>
</head>
<body>

<svg width="0" height="0" style="position:absolute">
  <symbol id="phone" viewBox="0 0 24 24"><path d="M6.6 3.5l3 .2 1.4 4-2 1.6a12 12 0 0 0 5.7 5.7l1.6-2 4 1.4.2 3c0 1.2-1 2.1-2.2 2A17 17 0 0 1 4.6 5.7c-.1-1.2.8-2.2 2-2.2z" fill="none" stroke="currentColor" stroke-width="1.8" stroke-linejoin="round"/></symbol>
</svg>

<!-- header -->
<div class="abs topbar">
  <span class="phone"><svg width="12" height="12"><use href="#phone"/></svg>(888)-555-0142</span>
  <span class="dot"></span><span class="dot"></span><span class="dot"></span><span class="dot"></span>
</div>
<div class="abs brand" style="left:106px;top:16px"><span class="mark"></span>wirenexa</div>
<nav class="abs nav">
  <a class="active">Home</a><a>About us</a><a>Services</a><a>Location</a><a>Contact</a>
</nav>
<a class="btn btn-red" style="left:962px;top:34px;width:130px;height:31px">Request A Quote</a>

<!-- hero -->
<div class="abs hero" role="img" aria-label="Server rack with patch panels and network cables"></div>
<h1 class="abs hero-title">Professional Cabling For Computers, Security Cameras, Wi-Fi, VOIP Phones, Access Control, Video and Audio</h1>
<a class="btn btn-red" style="left:106px;top:442px;width:130px">Request A Quote</a>
<a class="btn btn-outline" style="left:244px;top:442px;width:136px;border:none"><svg><use href="#phone"/></svg>(888)-555-0142</a>

<svg class="abs" style="left:0;top:500px" width="1200" height="220" viewBox="0 0 1200 220">
  <path d="M0,150 C250,60 480,10 720,40 C920,65 1070,140 1200,215 L1200,220 L0,220Z" fill="var(--red)"/>
  <path d="M0,150 C250,95 480,70 720,88 C920,102 1060,170 1200,220 L0,220Z" fill="var(--light)"/>
</svg>

<div class="abs quote-frame"></div>
<form class="abs quote-card">
  <h3>Request a Quote</h3>
  <p>Fill in the form below and we'll call you.</p>
  <div class="field">Name</div>
  <div class="field">Phone</div>
  <div class="field">Email...</div>
  <div class="field area">How can we help you?</div>
  <div class="submit">Get A Quote</div>
  <div class="callus">Call Us: <span class="ic"><svg width="11" height="11" style="color:var(--red)"><use href="#phone"/></svg></span>(888)-555-0142</div>
</form>

<!-- why choose us -->
<div class="abs section-light" style="top:720px;height:330px"></div>
<div class="eyebrow" style="top:692px">CABLE EXPERTS</div>
<h2 class="heading" style="top:713px">Why choose us</h2>

<div class="abs why-card" style="left:200px">
  <svg viewBox="0 0 40 40" fill="none" stroke="var(--red)" stroke-width="2.4" stroke-linejoin="round"><path d="M20 4l13 5v10c0 8-6 14-13 17C13 33 7 27 7 19V9z"/><path d="M14 20l4 4 8-9"/></svg>
  <h4>Safe &amp; Secure</h4>
  <p>Lorem Ipsum is simply dummy text of the printing and typesetting industry.</p>
</div>
<div class="abs why-card" style="left:475px">
  <svg viewBox="0 0 40 40" fill="none" stroke="var(--red)" stroke-width="2.4"><circle cx="20" cy="16" r="7"/><path d="M9 18a11 11 0 0 1 22 0M9 18v5h4M31 18v5h-4M27 23c0 4-3 7-7 7"/><path d="M8 36c2-5 6-7 12-7s10 2 12 7"/></svg>
  <h4>24×7 Support</h4>
  <p>Lorem Ipsum is simply dummy text of the printing and typesetting industry.</p>
</div>
<div class="abs why-card" style="left:750px">
  <svg viewBox="0 0 40 40" fill="none" stroke="var(--red)" stroke-width="2.4"><rect x="14" y="4" width="20" height="26" rx="3"/><path d="M19 11h10M19 17h10M19 23h6"/><ellipse cx="12" cy="24" rx="7" ry="3"/><path d="M5 24v8c0 2 3 3 7 3s7-1 7-3v-8M5 28c0 2 3 3 7 3s7-1 7-3"/></svg>
  <h4>Low Cost</h4>
  <p>Lorem Ipsum is simply dummy text of the printing and typesetting industry.</p>
</div>
<a class="btn btn-red" style="left:462px;top:943px;width:132px">Request A Quote</a>
<a class="btn btn-outline" style="left:600px;top:943px;width:138px"><svg><use href="#phone"/></svg>(888)-555-0142</a>

<!-- about -->
<div class="abs about-photo" role="img" aria-label="Close-up of a patch panel with blue and orange network cables"></div>
<div class="abs about">
  <div class="eyebrow">WELCOME TO</div>
  <h2>Wirenexa</h2>
  <h5>Elevate Your Connectivity with Wirenexa's Low Voltage Cabling Solutions</h5>
  <p>Wirenexa is your premier provider of professional low voltage cabling services in Virginia, Washington DC, and Maryland. With a focus on quality, reliability, and attention to detail, we deliver exceptional cabling solutions for audio, video, security systems, computer networks, and more...</p>
  <a class="btn btn-black">Explore More</a>
</div>

<!-- services -->
<div class="abs section-light" style="top:1520px;height:1200px;background:linear-gradient(160deg,#f3f2f3,#e9e8ea 50%,#f3f2f3)"></div>
<svg class="abs" style="left:0;top:1500px" width="1200" height="160" viewBox="0 0 1200 160">
  <path d="M0,0 H1200 V20 C1050,5 850,40 660,70 C520,92 300,120 0,100Z" fill="#fff"/>
  <path d="M0,88 C250,110 450,95 650,65 C470,100 260,130 0,120Z" fill="var(--red)"/>
</svg>
<div class="eyebrow" style="top:1700px">WHAT WE DO</div>
<h2 class="heading" style="top:1723px">Professional low voltage<br>cabling services</h2>

<div class="abs svc-text" style="left:106px;top:1890px;width:260px">
  <h3>Commercial services</h3>
  <p>Complete office low voltage cabling and Wi-Fi for your network and security system.</p>
  <a class="btn btn-black">Contact Us</a>
</div>
<div class="photo" style="left:507px;top:1842px;width:18px;height:200px;background:var(--red)"></div>
<div class="photo" role="img" aria-label="Modern open office meeting room with glass partitions" style="left:525px;top:1842px;width:568px;height:373px;border-top-right-radius:46px;background:linear-gradient(120deg,#7a5a4a 0%,#5c5550 35%,#8c8a86 65%,#b9bcc0 100%)"></div>

<div class="photo" style="left:675px;top:2292px;width:18px;height:225px;background:#2c2c2c"></div>
<div class="photo" role="img" aria-label="Industrial plant with silos at dusk by the water" style="left:106px;top:2142px;width:569px;height:375px;border-bottom-left-radius:46px;background:linear-gradient(180deg,#4f7fc0 0%,#3d6aa6 45%,#2d3d52 75%,#1f2a36 100%)"></div>
<div class="abs svc-text" style="left:762px;top:2292px;width:260px">
  <h3>Industrial services</h3>
  <p>Structured cabling, IDF and MDF for warehouses, manufacturing facilities and others.</p>
  <a class="btn btn-black">Contact Us</a>
</div>
<a class="btn btn-red" style="left:462px;top:2549px;width:132px">Request A Quote</a>
<a class="btn btn-outline" style="left:600px;top:2549px;width:138px"><svg><use href="#phone"/></svg>(888)-555-0142</a>

<svg class="abs" style="left:0;top:2630px" width="1200" height="170" viewBox="0 0 1200 170">
  <path d="M0,60 C300,95 520,80 760,30 C900,5 1080,20 1200,85 V170 H0Z" fill="#fff"/>
  <path d="M560,70 C700,30 880,-5 1010,15 C1100,30 1170,60 1200,90 V110 C1150,70 1050,35 940,30 C820,25 700,50 560,70Z" fill="var(--red)"/>
</svg>

<!-- projects -->
<div class="eyebrow" style="top:2847px">CABLING SOLUTIONS</div>
<h2 class="heading" style="top:2876px">Very professional structured low voltage<br>cabling projects for</h2>
<div class="abs proj" style="left:200px"><div class="ph" role="img" aria-label="Wi-Fi router on a desk beside a laptop" style="background:linear-gradient(180deg,#cfcfcf,#8d8d8d)"></div><span>Wi-Fi</span></div>
<div class="abs proj" style="left:406px"><div class="ph" role="img" aria-label="Conference room with screens and desks" style="background:linear-gradient(180deg,#7d7e80,#3b3c3e)"></div><span>Audio/Video<br>Conference Rooms</span></div>
<div class="abs proj" style="left:611px"><div class="ph" role="img" aria-label="Access control keypad on a glass door" style="background:linear-gradient(160deg,#e9dcc0,#b9a27a 60%,#8c7a5a)"></div><span>Access Control<br>Systems</span></div>
<div class="abs proj" style="left:818px"><div class="ph" role="img" aria-label="Security camera in a bright office" style="background:linear-gradient(180deg,#dfe7ef,#9fb4c8)"></div><span>CCTV</span></div>
<a class="btn btn-red" style="left:462px;top:3213px;width:132px">Request A Quote</a>
<a class="btn btn-outline" style="left:600px;top:3213px;width:138px"><svg><use href="#phone"/></svg>(888)-555-0142</a>

<!-- locations -->
<div class="abs section-light" style="top:3318px;height:520px"></div>
<div class="eyebrow" style="top:3395px">LOCATION</div>
<h2 class="heading" style="top:3421px">Services area</h2>
<div class="abs loc" role="img" aria-label="Virginia city skyline at dusk" style="left:200px;background:linear-gradient(180deg,#a98f8f,#6e5a5a 60%,#3b3030)"><span class="tag">VIRGINIA</span></div>
<div class="abs loc" role="img" aria-label="Capitol building in Washington DC" style="left:475px;background:linear-gradient(180deg,#9ec0e6,#c9d6e0 55%,#8a6f4e)"><span class="tag">WASHINGTON DC</span></div>
<div class="abs loc" role="img" aria-label="Baltimore harbor skyline in Maryland" style="left:750px;background:linear-gradient(180deg,#6fa3dc,#5d7fa8 55%,#3a5d7a)"><span class="tag">MARYLAND</span></div>
<a class="btn btn-red" style="left:462px;top:3693px;width:132px">Request A Quote</a>
<a class="btn btn-outline" style="left:600px;top:3693px;width:138px"><svg><use href="#phone"/></svg>(888)-555-0142</a>

<!-- footer -->
<svg class="abs" style="left:0;top:3760px" width="1200" height="140" viewBox="0 0 1200 140">
  <path d="M0,110 C220,100 420,40 640,15 C840,-5 1040,10 1200,40 V140 H0Z" fill="var(--black)"/>
  <path d="M0,100 C200,95 380,60 560,30 C400,75 220,115 0,125Z" fill="var(--red)"/>
</svg>
<div class="abs footer"></div>
<div class="abs brand" style="left:495px;top:3985px;color:#fff;font-size:29px"><span class="mark" style="width:30px;height:30px"></span>wirenexa</div>
<nav class="abs foot-nav">
  <a class="active">Home</a><i>/</i><a>About Us</a><i>/</i><a>Services</a><i>/</i><a>Location</a><i>/</i><a>Contact Us</a><i>/</i><a>Terms and Condition</a><i>/</i><a>Privacy Policy</a>
</nav>

<div class="abs contact" style="left:194px">
  <div class="ring"><svg style="color:var(--red)"><use href="#phone"/></svg></div>
  <h6>Phone</h6><p>(888)-555-0142</p>
</div>
<div class="abs divider" style="left:462px"></div>
<div class="abs contact" style="left:469px">
  <div class="ring"><svg viewBox="0 0 24 24" fill="none" stroke="var(--red)" stroke-width="1.8"><path d="M3 10l9-6 9 6v10H3z"/><path d="M3 10l9 6 9-6"/></svg></div>
  <h6>E-mail</h6><p>sales@wirenexa.com</p>
</div>
<div class="abs divider" style="left:738px"></div>
<div class="abs contact" style="left:744px">
  <div class="ring"><svg viewBox="0 0 24 24" fill="none" stroke="var(--red)" stroke-width="1.8"><path d="M12 21s-7-7-7-12a7 7 0 0 1 14 0c0 5-7 12-7 12z"/><circle cx="12" cy="9" r="2.5"/></svg></div>
  <h6>Address</h6><p>1420 Harbor Point Dr Suite 310<br>Reston, VA 20190</p>
</div>

<div class="abs socials-line" style="left:200px;width:320px"></div>
<div class="abs socials-line" style="left:680px;width:320px"></div>
<div class="abs socials"><span></span><span></span><span></span><span></span></div>
<p class="abs copy">© 2026 <b>Wirenexa</b>. All rights reserved.</p>

</body>
</html>
```